Morvek Menu

Hi there,
My restaurant called "Morvek" means Spice in hebrew.
We are middle eastern restaurant that specialist in dips,salads and hot bread baked on the spot and charcoal grilled meat skewers
The restaurant is pretty casual and the atmosphere is nice and customers feels like home.
on www.morvek.com.au you can see photos of the restaurant and the food.
ill add up the menus that i would like to be design please and the logo that is on the front of the shop is been add up
thank you

Target Market(s)

The regulars of the restaurant is jewish/israelis

Industry/Entity Type

Restaurant

```html
<!DOCTYPE html>
<html lang="en">
<head>
<meta charset="utf-8">
<title>Morvek – Lunch Menu Pages</title>
<link rel="stylesheet" href="https://fonts.googleapis.com/css2?family=Arimo:wght@700&family=Caveat:wght@600&family=Kalam:wght@400;700&family=Lora:ital,wght@0,400;1,700&display=swap">
<style>
  :root {
    --canvas: #ffffff;
    --board: #141414;
    --board-light: #2a2a2a;
    --panel: rgba(255,255,255,0.05);
    --chalk: #ffffff;
    --gold: #f4b731;
    --gold-deep: #f2a92a;
    --label: #111111;
    --rule: rgba(255,255,255,0.55);
    --food-a: #6b4a2a;
    --food-b: #b9a47e;
    --food-c: #c0653a;
  }
  * { margin: 0; padding: 0; box-sizing: border-box; }
  html, body { width: 1200px; height: 1000px; overflow: hidden; background: var(--canvas); }
  .sheet { position: relative; width: 1200px; height: 1000px; }

  .page {
    position: absolute; top: 103px; width: 561px; height: 793px; overflow: hidden;
    background: radial-gradient(ellipse at 55% 35%, var(--board-light) 0%, var(--board) 60%, #0a0a0a 100%);
    color: var(--chalk);
  }
  .page--three { left: 31px; }
  .page--four { left: 605px; width: 562px; }
  .page > * { position: absolute; }

  .page-label {
    position: absolute; top: 917px; font-family: Arimo, Arial, sans-serif; font-weight: 700;
    font-size: 22px; color: var(--label); width: 200px; text-align: center;
  }
  .page-label--three { left: 211px; }
  .page-label--four { left: 786px; }

  /* header */
  .brand-panel { left: 54px; top: 0; width: 280px; height: 197px; background: var(--panel); }
  .brand-name { left: 77px; top: 24px; font-family: Lora, Georgia, serif; font-size: 64px; line-height: 1; white-space: nowrap; }
  .brand-band { left: 69px; top: 103px; width: 250px; height: 88px;
    border-top: 3px solid var(--chalk); border-bottom: 3px solid var(--chalk);
    background: linear-gradient(90deg, #3a3a3a, #555 50%, #3a3a3a); }
  .contact { left: 344px; top: 91px; font-family: Lora, Georgia, serif; font-style: italic; font-weight: 700; font-size: 8px; line-height: 10px; white-space: nowrap; }
  .contact__line { display: flex; align-items: center; gap: 6px; font-size: 12px; margin-top: 6px; }
  .contact__icon { width: 14px; height: 14px; flex: none; }
  .contact__square { width: 13px; height: 13px; background: #3b5b9a; flex: none; }
  .contact__hours { margin-top: 10px; }

  .menu-title { left: 62px; top: 222px; font-family: Caveat, cursive; font-size: 60px; line-height: 1; }
  .entree { left: 64px; top: 298px; font-family: Kalam, cursive; font-weight: 700; font-size: 44px; line-height: 1; color: var(--gold-deep); }

  .heading { font-family: Kalam, cursive; font-size: 24px; line-height: 28px; font-weight: 400; white-space: nowrap; }
  .note { font-family: Lora, Georgia, serif; font-style: italic; font-size: 10px; line-height: 12px; white-space: nowrap; }
  .list { font-family: Arimo, Arial, sans-serif; font-weight: 700; font-size: 12px; line-height: 16px; color: var(--gold); white-space: nowrap; }
  .row { display: flex; }
  .row span:first-child { flex: none; }
  .rule { height: 0; border-top: 1px dashed var(--rule); }

  .food { background: radial-gradient(ellipse at 60% 80%, var(--food-c) 0%, var(--food-a) 35%, rgba(20,20,20,0) 75%); opacity: 0.75; }
  .food--four { background: radial-gradient(ellipse at 55% 85%, var(--food-b) 0%, var(--food-a) 40%, rgba(20,20,20,0) 78%); opacity: 0.6; }
</style>
</head>
<body>
<div class="sheet">

  <!-- Page 3 -->
  <section class="page page--three">
    <div class="food" role="img" aria-label="Photo of falafel, hummus and salad dishes" style="left:0;top:590px;width:561px;height:203px;"></div>
    <div class="brand-panel"></div>
    <div class="brand-name">Morvek</div>
    <div class="brand-band" role="img" aria-label="Decorative geometric star band"></div>
    <div class="contact">
      <div>Always Connected with us</div>
      <div class="contact__line">
        <svg class="contact__icon" viewBox="0 0 14 14"><circle cx="7" cy="7" r="7" fill="#3f8fd1"/><path d="M4.5 3.5l1.6 1.8-.8 1c.5 1 1.3 1.8 2.3 2.3l1-.8 1.8 1.6-1 1.3C6.6 10.5 3.5 7.4 3.3 4.6z" fill="#fff"/></svg>
        <span>99180432</span></div>
      <div class="contact__line"><span class="contact__square"></span><span>Morvek</span></div>
      <div class="contact__hours">Sunday - Friday 11:30-9:30<br>Saturday from 5:30-10.00<br>412 Harlow Road, Elmford South</div>
    </div>
    <div class="menu-title">Lunch Menu</div>
    <div class="entree">Entrée</div>

    <h2 class="heading" style="left:64px;top:356px;">Starters</h2>
    <div class="list" style="left:64px;top:387px;">
      <div class="row"><span style="width:316px">Falafel Balls</span><span>$5.00</span></div>
      <div class="row"><span style="width:316px">Moroccan Beef Cigars (3 per serve)</span><span>$11.00</span></div>
      <div class="row"><span style="width:316px">Fried Cauliflower</span><span>$8.00</span></div>
      <div class="row"><span style="width:316px">Pan Fried Mushrooms and Onions</span><span>$8.00</span></div>
      <div class="row"><span style="width:316px">Lamb Kibbeh &amp; Pinenuts (3 per serve)</span><span>$7.50</span></div>
    </div>
    <div class="rule" style="left:64px;top:480px;width:365px;"></div>

    <h2 class="heading" style="left:64px;top:493px;">Hummus Plate</h2>
    <p class="note" style="left:64px;top:521px;">Served with 1 Laffa and MixedPickles</p>
    <div class="list" style="left:64px;top:537px;">
      <div class="row"><span style="width:321px">Masabacha – served with Tahini and whole Chickpeas</span><span>$11.90</span></div>
      <div class="row"><span style="width:321px">Ful– served with warm, crushed Fava Beans</span><span>$14.90</span></div>
      <div class="row"><span style="width:321px">Mushroom– served with Pan Fried Mushrooms</span><span>$14.90</span></div>
      <div class="row"><span style="width:321px">Basar– served with Mince Lamb &amp; Pine nuts</span><span>$16.50</span></div>
    </div>
    <div class="rule" style="left:64px;top:613px;width:365px;"></div>

    <h2 class="heading" style="left:64px;top:625px;">Salads &amp; Dips Platter</h2>
    <p class="note" style="left:64px;top:653px;">3 Choices &amp; Laffa for $15.00 or 6 choices &amp; 2 Laffa for $28.00</p>
    <div class="list" style="left:64px;top:673px;">
      <div>Hummus</div><div>Tahini</div><div>Baba Ganoush</div><div>White Cabbage</div><div>Chatzilim (Fried Eggplant)</div>
    </div>
    <div class="list" style="left:231px;top:675px;">
      <div>Noa's Corn Salad</div><div>Moroccan Carrot</div><div>Roasted Beetroot</div><div>Turkish Dip</div><div>Mixed Pickles</div>
    </div>
  </section>

  <!-- Page 4 -->
  <section class="page page--four">
    <div class="food food--four" role="img" aria-label="Photo of fried schnitzel pieces and salad" style="left:0;top:600px;width:562px;height:193px;"></div>
    <div class="brand-panel"></div>
    <div class="brand-name">Morvek</div>
    <div class="brand-band" role="img" aria-label="Decorative geometric star band"></div>
    <div class="contact">
      <div>Always Connected with us</div>
      <div class="contact__line">
        <svg class="contact__icon" viewBox="0 0 14 14"><circle cx="7" cy="7" r="7" fill="#3f8fd1"/><path d="M4.5 3.5l1.6 1.8-.8 1c.5 1 1.3 1.8 2.3 2.3l1-.8 1.8 1.6-1 1.3C6.6 10.5 3.5 7.4 3.3 4.6z" fill="#fff"/></svg>
        <span>99180432</span></div>
      <div class="contact__line"><span class="contact__square"></span><span>Morvek</span></div>
      <div class="contact__hours">Sunday - Friday 11:30-9:30<br>Saturday from 5:30-10.00<br>412 Harlow Road, Elmford South</div>
    </div>
    <div class="menu-title">Lunch Menu</div>

    <h2 class="heading" style="left:71px;top:304px;">Israeli Lunch Tasting Plates</h2>
    <p class="note" style="left:71px;top:332px;">All tasting plates include a Chef's Selection of 4 Salads &amp; Dips and Laffa</p>
    <div class="list" style="left:71px;top:348px;">
      <div class="row"><span style="width:171px">Chicken Shashlik Plate</span><span>$10</span></div>
      <div class="row"><span style="width:171px">Lamb Shashlik Plate</span><span>$11.50</span></div>
      <div class="row"><span style="width:169px">Kebab (Kofta) Shashlik Plate</span><span>$10.00</span></div>
    </div>
    <div class="list" style="left:313px;top:348px;">
      <div class="row"><span style="width:127px">Chicken Liver Plate</span><span>$9.50</span></div>
      <div class="row"><span style="width:127px">Schnitzel Plate</span><span>$11.00</span></div>
      <div class="row"><span style="width:127px">Falafel Plate</span><span></span></div>
    </div>
    <div class="rule" style="left:71px;top:405px;width:410px;"></div>

    <h2 class="heading" style="left:71px;top:410px;">Wraps</h2>
    <p class="note" style="left:71px;top:437px;">Fresh Laffa wrap withHummus, Tahini, Israeli salad &amp; Mixed Pickles (Chilli optional)</p>
    <div class="list" style="left:71px;top:450px;">
      <div class="row"><span style="width:167px">Falafel wrap</span><span>$12</span></div>
      <div class="row"><span style="width:167px">Chicken wrap</span><span>$14</span></div>
      <div class="row"><span style="width:167px">Schnitzel wrap</span><span>$14</span></div>
    </div>
    <div class="list" style="left:313px;top:450px;">
      <div class="row"><span style="width:127px">Kofta wrap</span><span>$14</span></div>
      <div class="row"><span style="width:127px">Lamb wrap</span><span>$15</span></div>
    </div>
    <div class="rule" style="left:71px;top:506px;width:410px;"></div>

    <h2 class="heading" style="left:71px;top:515px;">Individual Shashlik</h2>
    <p class="note" style="left:71px;top:541px;">(1 Per serve)</p>
    <div class="list" style="left:71px;top:557px;">
      <div class="row"><span style="width:167px">Chicken Shashlik</span><span>$10</span></div>
      <div class="row"><span style="width:167px">Lamb Shashlik</span><span>$11.50</span></div>
      <div class="row"><span style="width:167px">Kebab (Kofta) Shashlik</span><span>$10.00</span></div>
    </div>
    <div class="list" style="left:313px;top:557px;">
      <div class="row"><span style="width:127px">Chicken Liver</span><span>$9.50</span></div>
      <div class="row"><span style="width:127px">Schnitzel</span><span>$11.00</span></div>
    </div>
    <div class="rule" style="left:71px;top:615px;width:410px;"></div>

    <h2 class="heading" style="left:71px;top:623px;">Kids Meal</h2>
    <p class="note" style="left:71px;top:650px;">(10 and under only)</p>
    <div class="list" style="left:71px;top:665px;">
      <div>Schnitzel plate with chips and</div>
      <div class="row"><span style="width:127px">Israeli Salad</span><span>$10.00</span></div>
      <div>Falafel Plate with chips and</div>
      <div class="row"><span style="width:127px">Israeli Salad</span><span>$9.00</span></div>
    </div>
    <div style="left:296px;top:625px;height:102px;border-left:1px dashed var(--rule);"></div>

    <h2 class="heading" style="left:312px;top:621px;">Sides</h2>
    <div class="list" style="left:312px;top:648px;">
      <div class="row"><span style="width:127px">Israeli Salad</span><span>$10.00</span></div>
      <div class="row"><span style="width:127px">Chips</span><span>$8.00</span></div>
      <div class="row"><span style="width:127px">Laffa</span><span>$2.50</span></div>
      <div class="row"><span style="width:127px">Mix Pickles</span><span>$6.00</span></div>
    </div>
  </section>

  <div class="page-label page-label--three">Page 3</div>
  <div class="page-label page-label--four">Page4</div>
</div>
</body>
</html>
```